Event Poster for Bar Sunday Live Music and Happy Hour

We are a bar. Every Sunday we have a HARBOUR HOURS event where we have live music and a Sunday Happy Hour. I would like a poster that promotes this weekly event in A4 and A3. Information the poster should include:Event Name: SUNDAY SESSIONSVenue: Copper Lantern 218-222 Marlow Rd PrestonDrink Specials: 3:00 pm - 5:00pmLive Music: 4:30pm -6:30pmAttached is our logo.

Target Market(s)

Both sexes 30-40 year olds

Industry/Entity Type

Hospitality

Font styles to use
Sans Serif

Colors

Designer to choose colors to be used in the design.

Requirements
Must have
• Event Name: HARBOUR HOURS
• Venue: Copper Lantern 218-222 Marlow Rd Preston
• Drink Specials: 3:00 pm - 5:00pm
• Live Music: 4:30pm -6:30pm
• Logo
Nice to have
• Open to different styles and ideas. Like colour.
Should not have
• It should not be too blokey are over the top bar-like.

```html
<!DOCTYPE html>
<html lang="en">
<head>
<meta charset="utf-8">
<title>Harbour Hours – Copper Lantern</title>
<link href="https://fonts.googleapis.com/css2?family=Audiowide&family=Exo+2:wght@600;700&display=swap" rel="stylesheet">
<style>
  :root {
    --night: #16121f;
    --magenta: #c2286f;
    --violet: #6a2a86;
    --deep: #221838;
    --disc: #1c1a1e;
    --white: #ffffff;
    --glow: #e9c8ff;
    --accent-red: #e23b41;
  }
  html, body {
    margin: 0;
    padding: 0;
    overflow: hidden;
    background: var(--night);
  }
  .poster {
    position: relative;
    width: 861px;
    height: 1200px;
    overflow: hidden;
    font-family: "Exo 2", "Arial", sans-serif;
    color: var(--white);
  }
  .backdrop {
    position: absolute;
    inset: 0;
    background:
      radial-gradient(ellipse 60% 40% at 20% 10%, rgba(220,40,110,.85), transparent 70%),
      radial-gradient(ellipse 50% 40% at 85% 35%, rgba(230,60,140,.7), transparent 70%),
      radial-gradient(ellipse 70% 30% at 50% 62%, rgba(140,60,160,.7), transparent 75%),
      linear-gradient(180deg, #b32766 0%, #8b2b82 40%, #5a2e7c 62%, #2a1d44 78%, #17122a 100%);
  }
  .stage {
    position: absolute;
    inset: 0;
  }
  .brand {
    position: absolute;
    left: 620px;
    top: 32px;
    width: 200px;
    height: 200px;
    border-radius: 50%;
    background: #0b0b0b;
    display: flex;
    align-items: center;
    justify-content: center;
    text-align: center;
    font-family: "Exo 2", sans-serif;
    font-weight: 600;
    font-size: 26px;
    line-height: 1.15;
    letter-spacing: 2px;
    color: var(--white);
  }
  .event-title {
    position: absolute;
    left: 0;
    width: 861px;
    text-align: center;
    font-family: "Audiowide", sans-serif;
    font-size: 100px;
    line-height: 1;
    color: #141414;
    -webkit-text-stroke: 3px var(--white);
    text-shadow: 0 0 14px rgba(255,255,255,.7), 0 0 4px rgba(233,200,255,.9);
    margin: 0;
  }
  .event-title span { display: block; }
  .event-title .line-1 { margin-top: 232px; }
  .event-title .line-2 { margin-top: 40px; }
  .info {
    position: absolute;
    left: 0;
    width: 861px;
    text-align: center;
    font-weight: 600;
    line-height: 1.2;
    margin: 0;
  }
  .info.music { top: 636px; font-size: 40px; }
  .info.drinks { top: 852px; font-size: 42px; }
  .venue {
    position: absolute;
    left: 0;
    top: 1062px;
    width: 861px;
    text-align: center;
    font-weight: 600;
    font-size: 37px;
    line-height: 1.35;
    color: var(--accent-red);
    margin: 0;
  }
</style>
</head>
<body>
<main class="poster">
  <div class="backdrop" role="img" aria-label="Glowing magenta and violet cosmic sky above dark purple mountains"></div>

  <svg class="stage" width="861" height="1200" viewBox="0 0 861 1200" aria-hidden="true">
    <defs>
      <radialGradient id="ring-glow" cx="50%" cy="50%" r="50%">
        <stop offset="80%" stop-color="#ffffff" stop-opacity="0"/>
        <stop offset="90%" stop-color="#f2dcff" stop-opacity=".55"/>
        <stop offset="100%" stop-color="#ffffff" stop-opacity="0"/>
      </radialGradient>
      <radialGradient id="flare" cx="50%" cy="50%" r="50%">
        <stop offset="0%" stop-color="#ffffff"/>
        <stop offset="30%" stop-color="#b9a6ff" stop-opacity=".8"/>
        <stop offset="100%" stop-color="#5a3cff" stop-opacity="0"/>
      </radialGradient>
      <radialGradient id="smudge" cx="50%" cy="50%" r="50%">
        <stop offset="55%" stop-color="#0f0d12" stop-opacity=".9"/>
        <stop offset="100%" stop-color="#0f0d12" stop-opacity="0"/>
      </radialGradient>
      <pattern id="dots" width="6" height="6" patternUnits="userSpaceOnUse">
        <circle cx="3" cy="3" r="1" fill="#2c2a30"/>
      </pattern>
    </defs>
    <circle class="halo" cx="432" cy="392" r="300" fill="url(#ring-glow)"/>
    <circle class="halo-ring" cx="432" cy="392" r="272" fill="none" stroke="#f4e6ff" stroke-width="3" opacity=".8"/>
    <circle class="disc" cx="432" cy="392" r="260" fill="var(--disc)"/>
    <circle class="disc-texture" cx="432" cy="392" r="260" fill="url(#dots)"/>
    <ellipse class="time-backing" cx="430" cy="694" rx="230" ry="90" fill="url(#smudge)"/>
    <line class="rule-short" x1="300" y1="786" x2="560" y2="786" stroke="#fff" stroke-width="2"/>
    <line class="rule-long" x1="166" y1="797" x2="694" y2="797" stroke="#fff" stroke-width="2"/>
    <ellipse class="flare" cx="430" cy="1014" rx="160" ry="14" fill="url(#flare)"/>
    <line class="flare-line" x1="200" y1="1014" x2="660" y2="1014" stroke="#cfc4ff" stroke-width="1" opacity=".6"/>
  </svg>

  <div class="brand">COPPER<br>LANTERN</div>

  <h1 class="event-title"><span class="line-1">HARBOUR</span><span class="line-2">HOURS</span></h1>

  <p class="info music">LIVE MUSIC:<br>4:30PM -6:30PM</p>
  <p class="info drinks">DRINK SPECIALS:<br>3:00 PM - 5:00PM</p>

  <p class="venue">COPPER LANTERN 218-222<br>MARLOW RD PRESTON</p>
</main>
</body>
</html>
```